Powerpt Design Template for QV7LM

A powerpt design template for QV7lm. A simple layout utilizing my company in the design. www.qv7lm.example . Please use the color pallet from the website and the name, etc. You can use general content from the website but I also need to be able to add slides and utilize the design for multiple purposes.

Target Market(s)

Education

Requirements
Must have
• utlize the design and colors from www.qv7lm.example
Nice to have
• use some general content from the website for "about" qv7lm. More importantly, i need to be able to add slides

```html
<!DOCTYPE html>
<html lang="en">
<head>
<meta charset="utf-8">
<title>QV7lm Presentation Template</title>
<link rel="stylesheet" href="https://fonts.googleapis.com/css2?family=Roboto+Condensed:wght@300;400;700&family=Open+Sans:wght@400;600;700&display=swap">
<style>
:root{
  --orange:#f26b3a;
  --orange-soft:#f4865c;
  --orange-pale:#f9b294;
  --gray:#6d6e70;
  --gray-dark:#58595b;
  --gray-light:#a7a9ac;
  --canvas:#e4e4e5;
  --white:#ffffff;
  --ink:#414042;
  --yellow:#f7c948;
}
*{margin:0;padding:0;box-sizing:border-box}
html,body{width:1200px;height:891px;overflow:hidden;background:var(--canvas)}
body{position:relative;font-family:"Open Sans",sans-serif;color:var(--ink)}
.slide{position:absolute;width:253px;height:142px;overflow:hidden;background:var(--white)}
.slide *{position:absolute}
.col-1{left:177px}.col-2{left:434px}.col-3{left:690px}
.row-1{top:6px}.row-2{top:154px}.row-3{top:301px}.row-4{top:447px}.row-5{top:594px}.row-6{top:743px}
.title{font-family:"Roboto Condensed",sans-serif;font-weight:300;font-size:7px;letter-spacing:.1px;color:var(--gray-dark);left:10px;top:11px;text-transform:uppercase;white-space:nowrap}
.title::after{content:"";position:absolute;left:0;top:9px;width:12px;height:.6px;background:var(--orange)}
.title.light{color:var(--white)}
.footer-bar{left:0;bottom:0;width:100%;height:4px;background:var(--gray)}
.footer-bar::after{content:"";position:absolute;right:4px;top:0;width:5px;height:4px;background:var(--orange)}
.footer-mark{left:5px;bottom:5px;font-family:"Roboto Condensed",sans-serif;font-size:4.5px;color:var(--orange);white-space:nowrap}
.brand{font-family:"Open Sans",sans-serif;font-weight:400;color:var(--gray);white-space:nowrap;display:flex;align-items:center;gap:3px}
.brand .dot{position:static;width:7px;height:7px;background:var(--orange);border-radius:50%}
.tiny{font-size:2.6px;line-height:3.4px;color:var(--gray-dark)}
.tiny.white{color:var(--white)}
.tiny.bold{font-weight:700}
.tiny.center{text-align:center}
.tiny.justify{text-align:justify}
.photo{background:linear-gradient(135deg,#cfc8c2,#8d8680)}
.photo.warm{background:linear-gradient(120deg,#d9b9a3,#a67e66)}
.photo.cool{background:linear-gradient(120deg,#c7d3de,#6f8597)}
.photo.gray{background:linear-gradient(135deg,#9b9b9d,#6a6b6d)}
.orange-wash{background:linear-gradient(135deg,var(--orange-soft),var(--orange))}
.heading{font-family:"Roboto Condensed",sans-serif;white-space:nowrap}
.icon-circle{width:18px;height:18px;border-radius:50%;background:var(--orange);border:1.5px solid var(--white)}
.icon-circle svg{left:3px;top:3px;width:9px;height:9px}
.label{font-family:"Roboto Condensed",sans-serif;font-size:3.4px;font-weight:700;color:var(--orange);white-space:nowrap}
.label.white{color:var(--white)}
</style>
</head>
<body>

<!-- 1 cover -->
<section class="slide col-1 row-1 cover">
  <div class="brand" style="left:17px;top:31px;font-size:11px"><span class="dot"></span>QV7lm</div>
  <div class="photo warm" role="img" aria-label="Photo of three students smiling together" style="left:0;top:56px;width:130px;height:66px"></div>
  <div class="orange-wash" style="left:100px;top:56px;width:153px;height:66px;background:linear-gradient(90deg,rgba(242,107,58,0),var(--orange) 55%)"></div>
  <div class="heading" style="right:12px;top:81px;font-size:10px;font-weight:700;color:var(--white)">WELCOME</div>
  <div class="heading" style="right:12px;top:93px;font-size:6px;font-weight:300;color:var(--white)">TO OUR PRESENTATION</div>
  <div class="tiny white" style="right:12px;top:102px">Ashford, March 25, 2017</div>
  <div class="tiny" style="left:17px;top:131px;font-size:2.2px;white-space:nowrap">© 2017 All rights reserved. Contents are confidential and may not be shared without the written consent of QV7lm.</div>
</section>

<!-- 2 contents -->
<section class="slide col-2 row-1 contents orange-wash">
  <div class="photo" role="img" aria-label="Faint photo of hands working at a desk" style="left:100px;top:0;width:153px;height:142px;opacity:.18"></div>
  <div class="heading" style="left:24px;top:37px;font-size:3.5px;color:var(--white)">TABLE OF</div>
  <div class="heading" style="left:24px;top:43px;font-size:9px;font-weight:300;color:var(--white)">CONTENTS</div>
  <div style="left:24px;top:56px;width:12px;height:.6px;background:var(--white)"></div>
  <div class="toc" style="left:44px;top:74px;width:200px;height:60px">
    <svg viewBox="0 0 200 60" width="200" height="60" style="left:0;top:0">
      <g fill="none" stroke="#fff" stroke-width=".8"><circle cx="5" cy="6" r="4.5"/><circle cx="5" cy="26" r="4.5"/><circle cx="5" cy="45" r="4.5"/><circle cx="97" cy="6" r="4.5"/><circle cx="97" cy="26" r="4.5"/><circle cx="97" cy="45" r="4.5"/></g>
      <g fill="#fff" font-family="Open Sans" font-size="3.4" text-anchor="middle"><text x="5" y="7.2">1</text><text x="5" y="27.2">1</text><text x="5" y="46.2">1</text><text x="97" y="7.2">1</text><text x="97" y="27.2">1</text><text x="97" y="46.2">1</text></g>
      <g fill="#fff" font-family="Open Sans" font-size="3" font-weight="700">
        <text x="14" y="5">LOREM IPSUM DOLOR SIT</text><text x="14" y="9">MET DOLOR SIT MET</text>
        <text x="14" y="25">LOREM IPSUM DOLOR SIT</text><text x="14" y="29">MET DOLOR SIT MET</text>
        <text x="14" y="44">LOREM IPSUM DOLOR SIT</text><text x="14" y="48">MET DOLOR SIT MET</text>
        <text x="106" y="5">LOREM IPSUM DOLOR SIT</text><text x="106" y="9">MET DOLOR SIT MET</text>
        <text x="106" y="25">LOREM IPSUM DOLOR SIT</text><text x="106" y="29">MET DOLOR SIT MET</text>
        <text x="106" y="44">LOREM IPSUM DOLOR SIT</text><text x="106" y="48">MET DOLOR SIT MET</text>
      </g>
    </svg>
  </div>
</section>

<!-- 3 vision & mission -->
<section class="slide col-3 row-1 vision">
  <div class="orange-wash" style="left:0;top:0;width:253px;height:77px"></div>
  <div class="photo" role="img" aria-label="Faint photo of hands pointing at charts" style="left:0;top:0;width:253px;height:77px;opacity:.15"></div>
  <div style="left:0;top:77px;width:253px;height:65px;background:var(--gray)"></div>
  <div class="title light" style="top:12px">Vision &amp; Mission</div>
  <div class="icon-circle" style="left:55px;top:68px;width:20px;height:20px">
    <svg viewBox="0 0 10 10" style="left:4px;top:4px"><g fill="none" stroke="#fff" stroke-width="1.2"><circle cx="3" cy="6" r="2"/><circle cx="7" cy="6" r="2"/><path d="M3 4 L4 2 M7 4 L6 2 M4.5 5.5 h1"/></g></svg>
  </div>
  <div class="icon-circle" style="left:158px;top:68px;width:20px;height:20px">
    <svg viewBox="0 0 10 10" style="left:4px;top:4px"><g fill="none" stroke="#fff" stroke-width="1.2"><path d="M1.5 7 A3.6 3.6 0 1 1 8.5 7"/><path d="M5 6 L7 3.5"/></g></svg>
  </div>
  <p class="tiny white center" style="left:25px;top:94px;width:80px;font-size:3.3px;line-height:4.2px">To provide state of the art logistics and supply chain solutions to the defined needs of our customers using the best people, processes and systems in creating efficient and effective results.</p>
  <p class="tiny white center" style="left:128px;top:94px;width:80px;font-size:3.3px;line-height:4.2px">To provide state of the art logistics and supply chain solutions to the defined needs of our customers using the best people, processes and systems in creating efficient and effective results.</p>
</section>

<!-- 4 about us -->
<section class="slide col-1 row-2 about-a">
  <div class="title">About us</div>
  <div class="orange-wash" style="left:0;top:47px;width:82px;height:46px"></div>
  <p class="tiny white bold" style="left:15px;top:62px;width:62px;font-size:2.4px">LOREM IPSUM DOLOR SIT MET CONSECTETUR ADIPISCING ELIT SED DO EIUSMOD TEMPOR INCIDIDUNT UT LABORE ET DOLORE MAGNA</p>
  <div class="photo cool" role="img" aria-label="Photo of hands using a tablet with charts" style="left:82px;top:47px;width:171px;height:46px"></div>
  <p class="tiny justify" style="left:82px;top:99px;width:160px">Lorem ipsum dolor sit amet, consectetur adipiscing elit, sed do eiusmod tempor incididunt ut labore et dolore magna aliqua. Ut enim ad minim veniam, quis nostrud exercitation ullamco laboris nisi ut aliquip ex ea commodo consequat. Duis aute irure dolor in reprehenderit in voluptate velit esse cillum dolore eu fugiat nulla pariatur.</p>
  <div class="footer-mark">QV7lm</div><div class="footer-bar"></div>
</section>

<!-- 5 about us -->
<section class="slide col-2 row-2 about-b">
  <div class="title">About us</div>
  <div class="orange-wash" style="left:87px;top:42px;width:166px;height:46px"></div>
  <div class="photo warm" role="img" aria-label="Photo of books and an apple on a library desk" style="left:12px;top:34px;width:76px;height:60px"></div>
  <p class="tiny white bold" style="left:100px;top:52px;width:145px;font-size:2.4px">Lorem ipsum dolor sit amet, consectetur adipiscing elit, sed do eiusmod tempor incididunt ut labore et dolore magna aliqua. Ut enim ad minim veniam, quis nostrud exercitation ullamco laboris nisi ut aliquip ex ea commodo consequat. Duis aute irure dolor in reprehenderit in voluptate velit esse cillum dolore eu fugiat nulla pariatur.</p>
  <p class="tiny justify" style="left:100px;top:96px;width:145px">Lorem ipsum dolor sit amet, consectetur adipiscing elit, sed do eiusmod tempor incididunt ut labore et dolore magna aliqua. Ut enim ad minim veniam, quis nostrud exercitation ullamco laboris nisi ut aliquip ex ea commodo consequat. Duis aute irure dolor in reprehenderit in voluptate velit esse cillum dolore eu fugiat nulla pariatur. Excepteur sint occaecat cupidatat non proident, sunt in culpa qui officia deserunt mollit anim id est laborum.</p>
  <div class="footer-mark">QV7lm</div><div class="footer-bar"></div>
</section>

<!-- 6 about us -->
<section class="slide col-3 row-2 about-c">
  <div class="title">About us</div>
  <div class="photo cool" role="img" aria-label="Photo of business people shaking hands" style="left:12px;top:39px;width:53px;height:34px"></div>
  <p class="tiny center" style="left:12px;top:76px;width:53px;color:var(--orange)">Lorem ipsum dolor sit amet consectetur adipiscing elit sed do eiusmod</p>
  <p class="tiny justify" style="left:75px;top:39px;width:79px">Lorem ipsum dolor sit amet, consectetur adipiscing elit, sed do eiusmod tempor incididunt ut labore et dolore magna aliqua. Ut enim ad minim veniam, quis nostrud exercitation ullamco laboris nisi ut aliquip ex ea commodo consequat. Duis aute irure dolor in reprehenderit in voluptate velit esse cillum dolore eu fugiat nulla pariatur.</p>
  <p class="tiny justify" style="left:163px;top:39px;width:79px">Lorem ipsum dolor sit amet, consectetur adipiscing elit, sed do eiusmod tempor incididunt ut labore et dolore magna aliqua. Ut enim ad minim veniam, quis nostrud exercitation ullamco laboris nisi ut aliquip ex ea commodo consequat. Duis aute irure dolor in reprehenderit in voluptate velit esse cillum dolore eu fugiat nulla pariatur.</p>
  <p class="tiny justify" style="left:75px;top:84px;width:79px">Lorem ipsum dolor sit amet, consectetur adipiscing elit, sed do eiusmod tempor incididunt ut labore et dolore magna aliqua. Ut enim ad minim veniam, quis nostrud exercitation ullamco laboris nisi ut aliquip ex ea commodo consequat. Duis aute irure dolor in reprehenderit in voluptate velit esse cillum dolore eu.</p>
  <p class="tiny justify" style="left:163px;top:84px;width:79px">Lorem ipsum dolor sit amet, consectetur adipiscing elit, sed do eiusmod tempor incididunt ut labore et dolore magna aliqua. Ut enim ad minim veniam, quis nostrud exercitation ullamco laboris nisi ut aliquip ex ea commodo consequat. Duis aute irure dolor in reprehenderit in voluptate velit esse cillum dolore eu.</p>
  <div class="footer-mark">QV7lm</div><div class="footer-bar"></div>
</section>

<!-- 7 services -->
<section class="slide col-1 row-3 services" style="background:var(--gray)">
  <div class="photo gray" role="img" aria-label="Faint photo of a hand sketching a network diagram" style="left:0;top:0;width:253px;height:142px;opacity:.35"></div>
  <div class="title light" style="top:11px">Our services</div>
  <div class="icon-circle" style="left:23px;top:55px;width:22px;height:22px"><svg viewBox="0 0 10 10" style="left:5px;top:5px"><g fill="none" stroke="#fff" stroke-width="1.2"><circle cx="5" cy="5" r="4"/><path d="M5 1 V5 H9"/></g></svg></div>
  <div class="icon-circle" style="left:86px;top:55px;width:22px;height:22px"><svg viewBox="0 0 10 10" style="left:5px;top:5px"><g fill="#fff"><path d="M0 4 L5 1.5 L10 4 L5 6.5Z"/><path d="M2.5 5.5 V8 Q5 9.5 7.5 8 V5.5 L5 7Z"/></g></svg></div>
  <div class="icon-circle" style="left:144px;top:55px;width:22px;height:22px"><svg viewBox="0 0 10 10" style="left:5px;top:5px"><g fill="none" stroke="#fff" stroke-width="1.3"><circle cx="5" cy="5" r="2"/><circle cx="5" cy="5" r="4" stroke-dasharray="1.5 1"/></g></svg></div>
  <div class="icon-circle" style="left:207px;top:55px;width:22px;height:22px"><svg viewBox="0 0 10 10" style="left:5px;top:5px"><g fill="none" stroke="#fff" stroke-width="1.1"><circle cx="5" cy="3" r="1.4"/><circle cx="2" cy="4" r="1.1"/><circle cx="8" cy="4" r="1.1"/><path d="M2.5 9 V6.5 Q5 4.8 7.5 6.5 V9 M0.5 8 V6.4 M9.5 8 V6.4"/></g></svg></div>
  <div class="label white" style="left:11px;top:81px;font-size:4px">LOREM IPSUM DOLOR</div>
  <div class="label white" style="left:73px;top:81px;font-size:4px">LOREM IPSUM DOLOR</div>
  <div class="label white" style="left:131px;top:81px;font-size:4px">LOREM IPSUM DOLOR</div>
  <div class="label white" style="left:194px;top:81px;font-size:4px">LOREM IPSUM DOLOR</div>
  <p class="tiny white bold center" style="left:11px;top:88px;width:46px">dolor sit amet, consectetur adipiscing elit, sed do eiusmod tempor incididunt ut labore et dolore magna aliqua.</p>
  <p class="tiny white bold center" style="left:74px;top:88px;width:46px">dolor sit amet, consectetur adipiscing elit, sed do eiusmod tempor incididunt ut labore et dolore magna aliqua.</p>
  <p class="tiny white bold center" style="left:132px;top:88px;width:46px">dolor sit amet, consectetur adipiscing elit, sed do eiusmod tempor incididunt ut labore et dolore magna aliqua.</p>
  <p class="tiny white bold center" style="left:195px;top:88px;width:46px">dolor sit amet, consectetur adipiscing elit, sed do eiusmod tempor incididunt ut labore et dolore magna aliqua.</p>
</section>

<!-- 8 about us boxes -->
<section class="slide col-2 row-3 about-d">
  <div class="title">About us</div>
  <div class="orange-wash" style="left:16px;top:36px;width:53px;height:34px"></div>
  <div class="orange-wash" style="left:71px;top:36px;width:53px;height:34px"></div>
  <div class="orange-wash" style="left:127px;top:36px;width:53px;height:34px"></div>
  <div style="left:183px;top:36px;width:53px;height:34px;background:var(--gray)"></div>
  <div style="left:16px;top:70px;width:53px;height:45px;background:var(--gray-light)"></div>
  <div style="left:71px;top:70px;width:53px;height:45px;background:var(--gray-light)"></div>
  <div style="left:127px;top:70px;width:53px;height:45px;background:var(--gray-light)"></div>
  <div style="left:183px;top:70px;width:53px;height:45px;background:var(--gray-light)"></div>
  <svg viewBox="0 0 10 10" width="10" height="10" style="left:37px;top:41px"><path d="M2 5 L5 1 L8 4 L6 5 L9 9 L5 7 L2 9Z" fill="#fff"/></svg>
  <svg viewBox="0 0 10 10" width="10" height="10" style="left:92px;top:41px"><circle cx="5" cy="5" r="4.2" fill="none" stroke="#fff"/><path d="M5 4 V8 M5 2.2 V3" stroke="#fff" stroke-width="1.1"/></svg>
  <svg viewBox="0 0 10 10" width="10" height="10" style="left:148px;top:41px"><path d="M0.5 4 L3 2.5 L5 4 L7 2.5 L9.5 4 L7.5 7 L5 8.5 L2.5 7Z" fill="#fff"/></svg>
  <svg viewBox="0 0 10 10" width="10" height="10" style="left:204px;top:41px"><g stroke="#fff" stroke-width=".8"><path d="M5 5 L5 1 M5 5 L1.5 3 M5 5 L8.5 3 M5 5 L2 8.5 M5 5 L8 8.5"/></g><circle cx="5" cy="5" r="1.4" fill="#fff"/></svg>
  <div class="label white center" style="left:16px;top:55px;width:53px;text-align:center;white-space:normal;font-size:3px">MANAGEMENT SOLUTIONS</div>
  <div class="label white center" style="left:71px;top:55px;width:53px;text-align:center;white-space:normal;font-size:3px">INFORMATION SOLUTIONS</div>
  <div class="label white center" style="left:127px;top:55px;width:53px;text-align:center;white-space:normal;font-size:3px">PROFESSIONAL SERVICES</div>
  <div class="label white center" style="left:183px;top:55px;width:53px;text-align:center;white-space:normal;font-size:3px">ORGANIZATIONAL TRANSFORMATION</div>
  <p class="tiny white bold center" style="left:20px;top:78px;width:45px">dolor sit amet, consectetur adipiscing elit, sed do eiusmod tempor incididunt ut labore et dolore magna aliqua.</p>
  <p class="tiny white bold center" style="left:75px;top:78px;width:45px">dolor sit amet, consectetur adipiscing elit, sed do eiusmod tempor incididunt ut labore et dolore magna aliqua.</p>
  <p class="tiny white bold center" style="left:131px;top:78px;width:45px">dolor sit amet, consectetur adipiscing elit, sed do eiusmod tempor incididunt ut labore et dolore magna aliqua.</p>
  <p class="tiny white bold center" style="left:187px;top:78px;width:45px">dolor sit amet, consectetur adipiscing elit, sed do eiusmod tempor incididunt ut labore et dolore magna aliqua.</p>
  <div class="footer-mark">QV7lm</div><div class="footer-bar"></div>
</section>

<!-- 9 partners -->
<section class="slide col-3 row-3 partners">
  <div class="title">Our partners</div>
  <svg viewBox="0 0 140 72" width="140" height="72" style="left:57px;top:42px" role="img" aria-label="Grid of partner badges">
    <g fill="#c9cacc">
      <rect x="2" y="4" width="22" height="8" rx="1" fill="#e2453c"/><rect x="40" y="4" width="22" height="8" rx="1" fill="#3d7a46"/><rect x="78" y="4" width="24" height="8" rx="1" fill="#2a3f7a"/><rect x="118" y="2" width="12" height="12" fill="#2a3f7a"/>
      <rect x="2" y="22" width="24" height="8" rx="1" fill="#5b8fd4"/><rect x="40" y="22" width="24" height="8" rx="1" fill="#333"/><rect x="78" y="22" width="22" height="8" rx="1" fill="#3f6b2f"/><rect x="118" y="21" width="12" height="10" rx="1" fill="#d93b2f"/>
      <rect x="2" y="39" width="18" height="9" rx="1" fill="#6b3fa0"/><circle cx="52" cy="43" r="4.5" fill="#f0a040"/><rect x="78" y="39" width="22" height="8" rx="4" fill="#8a8c8e"/><circle cx="124" cy="43" r="5" fill="#e8d27a"/>
      <rect x="2" y="56" width="26" height="7" rx="1" fill="#2a3f7a"/><rect x="40" y="56" width="26" height="7" rx="1" fill="#7d7f82"/><rect x="78" y="56" width="24" height="7" rx="1" fill="#2f54a8"/><circle cx="124" cy="60" r="5" fill="#9fb9d8"/>
    </g>
  </svg>
  <div class="footer-mark">QV7lm</div><div class="footer-bar"></div>
</section>

<!-- 10 chart bars -->
<section class="slide col-1 row-4 chart-bars">
  <div class="title">Our chart</div>
  <div class="tiny bold" style="left:20px;top:41px;color:var(--orange)">Lorem ipsum dolor sit amet</div>
  <p class="tiny justify" style="left:20px;top:45px;width:118px">consectetur adipiscing elit, sed do eiusmod tempor incididunt ut labore et dolore magna aliqua. Ut enim ad minim veniam, quis nostrud exercitation ullamco laboris nisi ut aliquip ex ea commodo consequat. Duis aute irure dolor in reprehenderit in voluptate velit esse cillum dolore.</p>
  <div class="tiny bold" style="left:20px;top:72px;color:var(--orange)">Lorem ipsum dolor sit amet</div>
  <p class="tiny justify" style="left:20px;top:76px;width:118px">consectetur adipiscing elit, sed do eiusmod tempor incididunt ut labore et dolore magna aliqua. Ut enim ad minim veniam, quis nostrud exercitation ullamco laboris nisi ut aliquip ex ea commodo consequat. Duis aute irure dolor in reprehenderit.</p>
  <div class="tiny bold" style="left:20px;top:101px;color:var(--orange)">Lorem ipsum dolor sit amet</div>
  <p class="tiny justify" style="left:20px;top:105px;width:118px">Excepteur sint occaecat cupidatat non proident, sunt in culpa qui officia deserunt mollit anim id est laborum sint occaecat cupidatat non.</p>
  <svg viewBox="0 0 80 50" width="80" height="50" style="left:157px;top:30px" role="img" aria-label="Bar chart of three series from 2009 to 2012">
    <g>
      <rect x="4" y="8" width="3" height="32" fill="var(--orange)"/><rect x="8" y="24" width="3" height="16" fill="var(--gray-light)"/><rect x="12" y="18" width="3" height="22" fill="var(--yellow)"/>
      <rect x="24" y="14" width="3" height="26" fill="var(--orange)"/><rect x="28" y="6" width="3" height="34" fill="var(--gray-light)"/><rect x="32" y="22" width="3" height="18" fill="var(--yellow)"/>
      <rect x="44" y="18" width="3" height="22" fill="var(--orange)"/><rect x="48" y="26" width="3" height="14" fill="var(--gray-light)"/><rect x="52" y="12" width="3" height="28" fill="var(--yellow)"/>
      <rect x="64" y="10" width="3" height="30" fill="var(--orange)"/><rect x="68" y="20" width="3" height="20" fill="var(--gray-light)"/><rect x="72" y="4" width="3" height="36" fill="var(--yellow)"/>
      <path d="M0 40 H80" stroke="#bbb" stroke-width=".4"/>
    </g>
    <g font-family="Open Sans" font-size="3" fill="#666" text-anchor="middle"><text x="10" y="46">2009</text><text x="30" y="46">2010</text><text x="50" y="46">2011</text><text x="70" y="46">2012</text></g>
  </svg>
  <div style="left:174px;top:85px;width:3px;height:3px;background:var(--orange)"></div>
  <div class="tiny bold" style="left:180px;top:84px">LOREMIPSUM</div>
  <p class="tiny" style="left:180px;top:88px;width:42px;font-size:2.2px;line-height:2.8px">consectetur adipiscing elit sed do eiusmod tempor</p>
  <div style="left:174px;top:99px;width:3px;height:3px;background:var(--gray-light)"></div>
  <div class="tiny bold" style="left:180px;top:98px">LOREMIPSUM</div>
  <p class="tiny" style="left:180px;top:102px;width:42px;font-size:2.2px;line-height:2.8px">consectetur adipiscing elit sed do eiusmod tempor</p>
  <div style="left:174px;top:113px;width:3px;height:3px;background:var(--yellow)"></div>
  <div class="tiny bold" style="left:180px;top:112px">LOREMIPSUM</div>
  <div class="footer-mark">QV7lm</div><div class="footer-bar"></div>
</section>

<!-- 11 chart donuts -->
<section class="slide col-2 row-4 chart-donuts">
  <div class="title">Our chart</div>
  <svg viewBox="0 0 253 40" width="253" height="40" style="left:0;top:40px" role="img" aria-label="Three donut charts at 81, 72 and 63 percent">
    <g fill="none" stroke-width="4">
      <circle cx="59" cy="19" r="15" stroke="var(--yellow)"/>
      <circle cx="59" cy="19" r="15" stroke="var(--orange)" stroke-dasharray="76.3 94.2" transform="rotate(-90 59 19)"/>
      <circle cx="133" cy="19" r="15" stroke="var(--orange)"/>
      <circle cx="133" cy="19" r="15" stroke="var(--yellow)" stroke-dasharray="67.8 94.2" transform="rotate(-90 133 19)"/>
      <circle cx="204" cy="19" r="15" stroke="var(--yellow)"/>
      <circle cx="204" cy="19" r="15" stroke="var(--orange)" stroke-dasharray="59.3 94.2" transform="rotate(-90 204 19)"/>
    </g>
    <g font-family="Roboto Condensed" font-weight="700" font-size="6" fill="var(--orange)" text-anchor="middle"><text x="59" y="21">81%</text><text x="133" y="21">72%</text><text x="204" y="21">63%</text></g>
  </svg>
  <p class="tiny center" style="left:34px;top:83px;width:50px">dolor sit amet, consectetur adipiscing elit, sed do eiusmod tempor incididunt ut labore et dolore magna aliqua. Ut enim ad minim veniam, quis nostrud ullamco laboris nisi ut aliquip ex ea commodo.</p>
  <p class="tiny center" style="left:108px;top:83px;width:50px">dolor sit amet, consectetur adipiscing elit, sed do eiusmod tempor incididunt ut labore et dolore magna aliqua. Ut enim ad minim veniam, quis nostrud ullamco laboris nisi ut aliquip ex ea commodo.</p>
  <p class="tiny center" style="left:179px;top:83px;width:50px">dolor sit amet, consectetur adipiscing elit, sed do eiusmod tempor incididunt ut labore et dolore magna aliqua. Ut enim ad minim veniam, quis nostrud ullamco laboris nisi ut aliquip ex ea commodo.</p>
  <div class="footer-mark">QV7lm</div><div class="footer-bar"></div>
</section>

<!-- 12 team -->
<section class="slide col-3 row-4 team">
  <div class="title">Our team</div>
  <div class="photo" role="img" aria-label="Portrait photo of a team member" style="left:35px;top:37px;width:30px;height:30px;border-radius:50%;border:1.5px solid var(--orange)"></div>
  <div class="photo warm" role="img" aria-label="Portrait photo of a team member" style="left:111px;top:37px;width:30px;height:30px;border-radius:50%;border:1.5px solid var(--orange)"></div>
  <div class="photo" role="img" aria-label="Portrait photo of a team member" style="left:191px;top:37px;width:30px;height:30px;border-radius:50%;border:1.5px solid var(--orange)"></div>
  <div class="label" style="left:36px;top:72px">JORDAN VALE</div><div class="tiny" style="left:42px;top:76px;font-size:2.2px">President</div>
  <div class="label" style="left:114px;top:72px">MIRA LUND</div><div class="tiny" style="left:114px;top:76px;font-size:2.2px">CEO / Founder</div>
  <div class="label" style="left:193px;top:72px">NORA QUILL</div><div class="tiny" style="left:194px;top:76px;font-size:2.2px">Vice President</div>
  <p class="tiny center" style="left:24px;top:82px;width:52px">dolor sit amet, consectetur adipiscing elit, sed do eiusmod tempor incididunt ut labore et dolore magna aliqua. Ut enim ad minim veniam, ullamco laboris nisi ut aliquip ex ea commodo.</p>
  <p class="tiny center" style="left:100px;top:82px;width:52px">dolor sit amet, consectetur adipiscing elit, sed do eiusmod tempor incididunt ut labore et dolore magna aliqua. Ut enim ad minim veniam, ullamco laboris nisi ut aliquip ex ea commodo.</p>
  <p class="tiny center" style="left:180px;top:82px;width:52px">dolor sit amet, consectetur adipiscing elit, sed do eiusmod tempor incididunt ut labore et dolore magna aliqua. Ut enim ad minim veniam, ullamco laboris nisi ut aliquip ex ea commodo.</p>
  <div class="footer-mark">QV7lm</div><div class="footer-bar"></div>
</section>

<!-- 13 infograph ring -->
<section class="slide col-1 row-5 infograph-a">
  <div class="title">Infograph</div>
  <svg viewBox="0 0 80 80" width="80" height="80" style="left:91px;top:38px" role="img" aria-label="Segmented half ring of six topics">
    <g stroke="#fff" stroke-width="1">
      <path d="M40 40 L4 40 A36 36 0 0 1 14.5 14.5Z" fill="var(--gray)"/>
      <path d="M40 40 L14.5 14.5 A36 36 0 0 1 40 4Z" fill="var(--orange)"/>
      <path d="M40 40 L40 4 A36 36 0 0 1 65.5 14.5Z" fill="var(--gray)"/>
      <path d="M40 40 L65.5 14.5 A36 36 0 0 1 76 40Z" fill="var(--orange)"/>
      <path d="M40 40 L76 40 A36 36 0 0 1 65.5 65.5Z" fill="var(--gray)"/>
      <path d="M40 40 L4 40 A36 36 0 0 0 14.5 65.5Z" fill="var(--orange)"/>
    </g>
    <circle cx="40" cy="40" r="17" fill="#fff"/>
    <rect x="14" y="40" width="52" height="40" fill="#fff" opacity="0"/>
    <g font-family="Open Sans" font-size="2.4" fill="#fff" font-weight="700" text-anchor="middle"><text x="16" y="33">Lorem ipsum</text><text x="31" y="16">Lorem ipsum</text><text x="51" y="16">Lorem ipsum</text><text x="64" y="33">Lorem ipsum</text></g>
  </svg>
  <div class="tiny" style="left:57px;top:40px;font-size:3.4px;color:var(--ink)">Lorem ipsum</div>
  <p class="tiny center" style="left:35px;top:45px;width:48px">Dolor sit amet, consectetur adipiscing elit, sed do eiusmod tempor</p>
  <div class="tiny" style="left:57px;top:69px;font-size:3.4px;color:var(--ink)">Lorem ipsum</div>
  <p class="tiny center" style="left:35px;top:74px;width:48px">Dolor sit amet, consectetur adipiscing elit, sed do eiusmod tempor</p>
  <div class="tiny" style="left:57px;top:98px;font-size:3.4px;color:var(--ink)">Lorem ipsum</div>
  <p class="tiny center" style="left:35px;top:103px;width:48px">Dolor sit amet, consectetur adipiscing elit, sed do eiusmod tempor</p>
  <div class="tiny" style="left:199px;top:40px;font-size:3.4px;color:var(--ink)">Lorem ipsum</div>
  <p class="tiny" style="left:187px;top:45px;width:48px">Dolor sit amet, consectetur adipiscing elit, sed do eiusmod tempor</p>
  <div class="tiny" style="left:199px;top:69px;font-size:3.4px;color:var(--ink)">Lorem ipsum</div>
  <p class="tiny" style="left:187px;top:74px;width:48px">Dolor sit amet, consectetur adipiscing elit, sed do eiusmod tempor</p>
  <div class="tiny" style="left:199px;top:98px;font-size:3.4px;color:var(--ink)">Lorem ipsum</div>
  <p class="tiny" style="left:187px;top:103px;width:48px">Dolor sit amet, consectetur adipiscing elit, sed do eiusmod tempor</p>
  <div class="footer-mark">QV7lm</div><div class="footer-bar"></div>
</section>

<!-- 14 infograph circle -->
<section class="slide col-2 row-5 infograph-b">
  <div class="title">Infograph</div>
  <svg viewBox="0 0 84 84" width="84" height="84" style="left:85px;top:32px" role="img" aria-label="Circular cycle of four topics">
    <g fill="none" stroke-width="16">
      <path d="M42 8 A34 34 0 0 1 76 42" stroke="var(--orange)"/>
      <path d="M76 42 A34 34 0 0 1 42 76" stroke="var(--gray)"/>
      <path d="M42 76 A34 34 0 0 1 8 42" stroke="var(--orange)"/>
      <path d="M8 42 A34 34 0 0 1 42 8" stroke="var(--gray)"/>
    </g>
    <g fill="#fff"><circle cx="42" cy="18" r="6"/><circle cx="66" cy="42" r="6"/><circle cx="42" cy="66" r="6"/><circle cx="18" cy="42" r="6"/></g>
    <g fill="none" stroke="var(--gray)" stroke-width=".8"><path d="M39 20 L45 15 L42 21Z"/><circle cx="66" cy="42" r="2.5"/><path d="M42 69 L39.5 65 A2.5 2.5 0 1 1 44.5 65Z"/><path d="M15.5 41 L18 38.5 L20.5 41 L18 45Z"/></g>
  </svg>
  <div class="tiny" style="left:24px;top:41px;font-size:3.6px;color:var(--orange)">Lorem ipsum</div>
  <p class="tiny center" style="left:22px;top:46px;width:48px">Dolor sit amet, consectetur adipiscing elit, sed do eiusmod tempor</p>
  <div class="tiny" style="left:24px;top:82px;font-size:3.6px;color:var(--ink)">Lorem ipsum</div>
  <p class="tiny center" style="left:22px;top:87px;width:48px">Dolor sit amet, consectetur adipiscing elit, sed do eiusmod tempor</p>
  <div class="tiny" style="left:198px;top:41px;font-size:3.6px;color:var(--ink)">Lorem ipsum</div>
  <p class="tiny" style="left:187px;top:46px;width:48px">Dolor sit amet, consectetur adipiscing elit, sed do eiusmod tempor</p>
  <div class="tiny" style="left:198px;top:82px;font-size:3.6px;color:var(--orange)">Lorem ipsum</div>
  <p class="tiny" style="left:187px;top:87px;width:48px">Dolor sit amet, consectetur adipiscing elit, sed do eiusmod tempor</p>
  <div class="footer-mark">QV7lm</div><div class="footer-bar"></div>
</section>

<!-- 15 infograph panel -->
<section class="slide col-3 row-5 infograph-c">
  <div class="orange-wash" style="left:16px;top:0;width:104px;height:142px"></div>
  <div class="photo warm" role="img" aria-label="Faint photo of pencils in a cup" style="left:16px;top:0;width:104px;height:90px;opacity:.25"></div>
  <div class="heading" style="left:25px;top:78px;font-size:4.5px;font-weight:700;color:var(--white)">Lorem ipsum dolor sit amet</div>
  <p class="tiny white" style="left:25px;top:86px;width:90px">Lorem ipsum dolor sit amet, consectetur adipiscing elit, sed do eiusmod tempor incididunt ut labore et dolore magna aliqua. Ut enim ad minim veniam, quis nostrud exercitation ullamco laboris nisi ut aliquip ex ea commodo consequat. Duis aute irure dolor in reprehenderit in voluptate velit esse cillum dolore eu fugiat nulla pariatur.</p>
  <div class="title" style="left:140px">Infograph</div>
  <svg viewBox="0 0 20 100" width="20" height="100" style="left:138px;top:38px">
    <g fill="none" stroke="var(--orange)" stroke-width=".8"><circle cx="10" cy="10" r="8"/><circle cx="10" cy="39" r="8"/><circle cx="10" cy="70" r="8"/></g>
    <g fill="none" stroke="var(--orange)" stroke-width="1"><circle cx="9" cy="9" r="3"/><path d="M11 11 L13.5 13.5"/><path d="M6 43 V39 M9 43 V36 M12 43 V38 M14 43 V40"/><circle cx="10" cy="71" r="3.5"/><path d="M10 66 V68 M10 71 L11.5 69.5"/></g>
  </svg>
  <p class="tiny" style="left:166px;top:43px;width:56px">Dolor sit amet, consectetur adipiscing elit, sed do eiusmod tempor</p>
  <p class="tiny" style="left:166px;top:72px;width:56px">Dolor sit amet, consectetur adipiscing elit, sed do eiusmod tempor</p>
  <p class="tiny" style="left:166px;top:103px;width:56px">Dolor sit amet, consectetur adipiscing elit, sed do eiusmod tempor</p>
  <div class="footer-bar"></div>
</section>

<!-- 16 image text -->
<section class="slide col-1 row-6 image-text">
  <div class="orange-wash" style="left:0;top:0;width:108px;height:142px"></div>
  <div class="photo cool" role="img" aria-label="Photo of two people reviewing a tablet by a window" style="left:108px;top:0;width:145px;height:142px"></div>
  <div class="title light" style="top:11px">Image text</div>
  <p class="tiny white justify" style="left:16px;top:55px;width:82px;font-size:2.8px;line-height:3.7px">Lorem ipsum dolor sit amet, consectetur adipiscing elit, sed do eiusmod tempor incididunt ut labore et dolore magna aliqua. Ut enim ad minim veniam, quis nostrud exercitation ullamco laboris nisi ut aliquip ex ea commodo consequat. Duis aute irure dolor in reprehenderit in voluptate velit esse cillum dolore eu fugiat nulla pariatur.</p>
  <div class="footer-mark" style="left:4px;bottom:3px;background:var(--white);padding:0 2px">QV7lm</div>
</section>

<!-- 17 section title -->
<section class="slide col-2 row-6 section-title" style="background:var(--gray)">
  <div class="photo gray" role="img" aria-label="Grayscale photo of a team meeting around a table" style="left:0;top:0;width:253px;height:142px"></div>
  <div style="left:0;top:0;width:253px;height:142px;background:rgba(90,90,92,.35)"></div>
  <div style="left:112px;top:56px;width:30px;height:30px;border-radius:50%;background:var(--orange);border:1.5px solid var(--white)"></div>
  <div class="heading" style="left:112px;top:57px;width:30px;text-align:center;font-family:Georgia,serif;font-style:italic;font-weight:700;font-size:20px;color:var(--white)">i</div>
  <div class="heading" style="left:100px;top:93px;font-size:7px;font-weight:300;color:var(--white)">SECTION TITLE</div>
</section>

<!-- 18 thank you -->
<section class="slide col-3 row-6 thank-you orange-wash">
  <div class="photo warm" role="img" aria-label="Faint photo of business people in discussion" style="left:0;top:0;width:253px;height:142px;opacity:.22"></div>
  <div style="left:31px;top:58px;width:58px;height:16px;background:var(--white)"></div>
  <div class="brand" style="left:36px;top:60px;font-size:9.5px"><span class="dot"></span>QV7lm</div>
  <div class="heading" style="left:31px;top:82px;font-size:6px;font-weight:300;color:var(--white)">THANK YOU</div>
  <svg viewBox="0 0 6 30" width="6" height="30" style="left:32px;top:96px"><g fill="#fff"><circle cx="3" cy="3" r="2.2"/><circle cx="3" cy="14" r="2.2"/><circle cx="3" cy="25" r="2.2"/></g></svg>
  <div class="tiny white bold" style="left:42px;top:97px;white-space:nowrap">120 Alder Row Suite 4</div>
  <div class="tiny white bold" style="left:42px;top:108px;white-space:nowrap">support@qv7lm.example</div>
  <div class="tiny white bold" style="left:42px;top:119px;white-space:nowrap">www.qv7lm.example</div>
</section>

</body>
</html>
```